Apply Existing Website Design to Wexmoor-Made Tele-Wellness App (UX/UI Work)

We’re looking for a highly skilled UX/UI designer to translate our existing website design into an intuitive, beautiful mobile app interface for our Wexmoor-developed tele-wellness platform. Hoping this designer will stay onboard with us for future work.

Scope of Work:
    •    Review our existing website design (style, colors, typography, components)
    •    Apply the same visual language to our mobile app screens
    •    Ensure consistent, user-friendly experience across the app
    •    Deliver high-fidelity mockups and design assets (preferably in Figma)
    •    Minimal UX rethinking may be needed to optimize for mobile, but the core brand and design system are already established

What We Provide:
    •    Access to the existing website design (including any style guides or component libraries)
    •    Wireframes or a basic functional map of the app screens
    •    Clear guidelines on branding and user flows

Ideal Candidate:
    •    Strong portfolio of mobile app design, especially healthcare/wellness preferred
    •    Proven experience in adapting web designs for mobile apps
    •    Expertise with Figma or comparable tools
    •    Attention to detail and commitment to brand consistency
    •    Ability to deliver quickly while maintaining quality

Deliverables:
    •    Complete set of high-fidelity, mobile-optimized app screens
    •    Organized design file (Figma preferred) ready for developer handoff
    •    Design assets as needed (icons, images, components)

Timeline:
    •    Estimated 1 week for initial delivery, with room for revisions

```html
<!DOCTYPE html>
<html lang="en">
<head>
<meta charset="utf-8">
<title>Verda — Holistic Tele-Wellness</title>
<link rel="stylesheet" href="https://fonts.googleapis.com/css2?family=Gilda+Display&family=Inter:wght@400;500;600;700&display=swap">
<style>
:root{
  --canvas:#fdd5aa;
  --peach:#f9cda0;
  --peach-soft:#fbd9b6;
  --peach-line:#f5c08c;
  --grey-1:#e5e5e5;
  --grey-2:#ececec;
  --card:#f5f5f5;
  --white:#ffffff;
  --ink:#1d1d1d;
  --ink-soft:#3f3f3f;
  --muted:#8c8c8c;
  --serif:"Gilda Display", Georgia, serif;
  --sans:"Inter", Arial, sans-serif;
}
*{box-sizing:border-box;margin:0;padding:0}
html,body{width:1200px;height:5000px;overflow:hidden}
body{background:var(--canvas);font-family:var(--sans);color:var(--ink)}
.page{position:absolute;left:385px;top:68px;width:430px;height:4860px;background:var(--grey-1);overflow:hidden}
.abs{position:absolute}
.center{left:0;right:0;text-align:center}
.serif{font-family:var(--serif)}

/* hero */
.hero{position:absolute;left:0;top:0;width:430px;height:485px;
  background:radial-gradient(ellipse 60% 45% at 62% 22%,#e9ece2 0%,#a9b39a 30%,#2f4a22 60%,#0b1408 85%),#060a05}
.hero::after{content:"";position:absolute;inset:0;background:linear-gradient(180deg,rgba(0,0,0,.05),rgba(0,0,0,.35) 60%,rgba(0,0,0,.15))}
.hero > *{z-index:1}
.brand{left:32px;top:36px;display:flex;align-items:center;gap:6px;font-family:var(--sans);font-weight:600;font-size:24px;letter-spacing:1px;color:var(--peach)}
.brand-dot{width:8px;height:8px;border-radius:50%;background:var(--peach)}
.menu{right:32px;top:42px;width:34px}
.menu span{display:block;height:3px;background:#fff;margin-bottom:7px;border-radius:2px}
.hero-title{top:172px;font-family:var(--serif);font-size:36px;line-height:42px;color:#fff}
.hero-sub{top:268px;font-size:15px;line-height:18px;color:#eee}
.hero-dev{top:334px;font-size:15px;font-weight:700;color:#fff}
.btn{display:flex;align-items:center;justify-content:center;background:var(--peach);color:var(--ink);border-radius:20px;font-size:15px;letter-spacing:.3px}
.hero .btn{left:123px;top:384px;width:184px;height:38px}

/* trust */
.trust{position:absolute;top:485px;left:0;width:430px;height:575px;background:var(--grey-1)}
.trust-by{top:36px;font-family:var(--serif);font-size:18px}
.trust-by b{font-family:var(--sans);font-weight:600;font-size:17px}
.trust-line{top:70px;font-size:12px;line-height:14px;color:var(--ink-soft)}
.quote-circle{left:74px;top:150px;width:282px;height:282px;border-radius:50%;background:var(--peach);text-align:center;padding:26px 40px 0}
.quote-dot{width:42px;height:42px;border-radius:50%;background:#000;margin:0 auto 14px}
.quote-role{font-size:11px;font-weight:700;line-height:14px;margin-bottom:12px}
.quote-body{font-size:11px;line-height:14px;color:var(--ink-soft)}
.quote-name{font-size:11px;margin-top:18px}
.metric{top:505px;font-size:12px}
.metric b{font-weight:700}

/* time tested */
.tested{position:absolute;top:1060px;left:0;width:430px;height:973px;background:var(--grey-2)}
.tested-title{top:28px;font-size:17px}
.tested-lead{top:60px;font-size:12.5px;line-height:15px;color:var(--ink-soft);padding:0 40px}
.pain{left:16px;width:399px;background:var(--card);text-align:center;padding:0 30px}
.pain svg{display:block;margin:10px auto 14px}
.pain h3{font-size:12px;font-weight:700;line-height:15px;margin-bottom:14px}
.pain p{font-size:12px;line-height:15px;color:var(--ink-soft)}
.tested .btn{left:124px;top:856px;width:184px;height:38px}
.tested-note{top:913px;font-size:12px;color:var(--ink-soft)}

/* difference */
.difference{position:absolute;top:2033px;left:0;width:430px;height:1157px;background:var(--grey-1)}
.diff-title{left:29px;top:30px;font-family:var(--serif);font-size:14px}
.diff-card{top:82px;height:97px;width:225px;background:var(--peach);border-radius:24px 0 24px 0;display:flex;align-items:flex-start;gap:10px;padding:16px 14px}
.diff-card h4{font-size:11px;font-weight:700;margin-bottom:6px}
.diff-card p{font-size:11px;line-height:14px;color:var(--ink-soft)}
.diff-icon{flex:none;width:32px;height:32px;border-radius:50%;background:#fff;display:flex;align-items:center;justify-content:center;margin-top:12px}
.wheel{left:0;top:230px;width:430px;height:380px}
.wheel-core{left:16px;top:81px;width:186px;height:186px;border-radius:50%;background:#f2f2f2;text-align:center;padding:30px 20px 0;font-size:6.5px;line-height:9px;color:var(--muted)}
.wheel-core b{display:block;font-weight:600;color:#6e6e6e;margin:4px 0 3px}
.wheel-item{font-size:7px;color:#555;display:flex;align-items:center;gap:10px}
.wheel-icon{width:30px;height:30px;border-radius:50%;background:var(--peach-soft);display:flex;align-items:center;justify-content:center}
.wheel-icon i{width:12px;height:12px;border:1.5px solid #c9864b;border-radius:3px}
.wheel-pill{left:169px;top:10px;width:180px;height:40px;background:#fff;border-radius:20px;padding-left:6px}
.divider{left:20px;width:390px;height:1px;background:#d3d3d3}
.step{left:20px;width:390px;height:80px}
.step-num{position:absolute;left:0;top:0;width:70px;height:70px;border-radius:50%;background:#f7f7f7;border:2px solid #fff;font-size:32px;color:#cfcfcf;display:flex;align-items:center;justify-content:center;box-shadow:0 1px 3px rgba(0,0,0,.05)}
.step svg{position:absolute;left:40px;top:-6px}
.step-dot{position:absolute;left:80px;top:30px;width:8px;height:8px;border-radius:50%;background:#000;border:2px solid #fff}
.step-text{position:absolute;left:102px;top:0;right:0}
.step-text h4{font-size:14px;font-weight:700;margin-bottom:12px}
.step-text p{font-size:12px;line-height:15px;color:var(--ink-soft)}

/* experts */
.experts{position:absolute;top:3090px;left:0;width:430px;height:1211px;background:var(--grey-1)}
.experts-title{top:40px;font-family:var(--serif);font-size:19px}
.experts-lead{top:70px;font-size:12px;line-height:15px;color:var(--ink-soft);padding:0 30px}
.doc{width:169px;height:190px;background:#fff;text-align:center;padding-top:16px}
.doc-photo{width:74px;height:74px;border-radius:50%;margin:0 auto 12px;background:radial-gradient(circle at 50% 40%,#b79b86,#5c4b40 70%,#3b3029)}
.doc h5{font-size:11.5px;font-weight:700;margin-bottom:3px}
.doc p{font-size:11.5px;line-height:14px;color:var(--ink-soft)}
.cert-title{top:620px;font-family:var(--serif);font-size:18px;line-height:21px}
.cert{top:693px;width:114px;height:136px;background:#fff;text-align:center;padding:14px 8px 0;font-size:11px;line-height:14px;font-weight:500}
.cert-mark{width:50px;height:50px;margin:0 auto 12px}
.bio-label{left:29px;top:902px;font-size:11.5px;font-weight:500;color:var(--ink-soft)}
.bio-photo{left:33px;top:941px;width:353px;height:103px;border-radius:0 40px 0 40px;background:radial-gradient(ellipse 30% 55% at 35% 50%,#ffd58a 0%,#c9874a 35%,#6a3b1e 70%,#2a160b 100%)}
.bio-text{left:31px;top:1067px;width:380px;font-size:11.5px;line-height:14.5px;color:#555}

/* footer */
.footer{position:absolute;top:4301px;left:0;width:430px;height:559px;
  background:radial-gradient(ellipse 55% 40% at 40% 55%,#b3577e 0%,#6b2e49 40%,transparent 70%),radial-gradient(ellipse 70% 60% at 60% 20%,#3b5a24,#16270d 70%),#0e1808}
.glass{left:23px;width:384px;background:rgba(255,255,255,.72);border-radius:18px;text-align:center}
.quote-card{top:68px;height:203px;padding:58px 22px 0}
.quote-badge{left:185px;top:37px;width:62px;height:62px;border-radius:50%;background:#fff;display:flex;align-items:center;justify-content:center}
.quote-card .small{font-size:11.5px;line-height:14px;color:#555}
.quote-card .big{font-family:var(--serif);font-size:19px;line-height:21px;margin:16px 0 14px}
.quote-card .sig{font-size:11px;color:#555}
.tree-card{top:293px;height:88px;text-align:left;padding:16px 22px 0;font-size:11.5px;line-height:14px;color:#222}
.contact{top:421px;font-size:17px;color:#fff}
.email{top:456px;font-size:12px;color:#fff}
.terms{top:488px;font-size:12px;color:#fff}
</style>
</head>
<body>
<main class="page">

  <section class="hero" role="img" aria-label="White magnolia flower on dark green foliage">
    <div class="abs brand"><span>VERDA</span><span class="brand-dot"></span></div>
    <div class="abs menu"><span></span><span></span><span></span></div>
    <h1 class="abs center hero-title">Holistic-Doctor led<br>care pay as you like</h1>
    <p class="abs center hero-sub">Evidence based care with heart<br>Tailored only for you Tele-Wellness</p>
    <p class="abs center hero-dev">Developed at Wexmoor</p>
    <a class="abs btn">BOOK NOW</a>
  </section>

  <section class="trust">
    <p class="abs center trust-by">Trusted by: <b>Northway Apparel™</b></p>
    <p class="abs center trust-line">Pioneers in corporate wellness: A Better<br>Way to Grow</p>
    <div class="abs quote-circle">
      <div class="quote-dot"></div>
      <p class="quote-role">Chief Strategy Officer,<br>National Tech Firm</p>
      <p class="quote-body">For the first time in 20 years of nonstop output, I found a wellness system that didn't just slow me down - it woke me up. Verda's personalized protocols gave me energy I didn't know I was missing, and more focused than ever before.</p>
      <p class="quote-name">Marcus</p>
    </div>
    <p class="abs center metric"><b>55</b> Million Bio-Markers analysed</p>
  </section>

  <section class="tested">
    <h2 class="abs center tested-title">Time Tested and Results Driven</h2>
    <p class="abs center tested-lead">We get it. You've tried the threads, the threads on the threads. It's time for something real- and built around you. Clarity is a form of care.</p>

    <article class="abs pain" style="top:145px;height:202px">
      <svg width="46" height="40" viewBox="0 0 46 40" fill="none" stroke="#f1b27a" stroke-width="2"><path d="M3 3h40v26H20l-9 8v-8H3z"/><circle cx="15" cy="16" r="1.5" fill="#f1b27a"/><circle cx="23" cy="16" r="1.5" fill="#f1b27a"/><circle cx="31" cy="16" r="1.5" fill="#f1b27a"/></svg>
      <h3>Conflicted by fad-driven advice and endless tests without real insights?</h3>
      <p>Verda cuts through the noise with tim-tested, evidence-based care and real credentials - thousands of years of wisdom versus a few years of fragmented information in holistic medicine</p>
    </article>

    <article class="abs pain" style="top:372px;height:202px">
      <svg width="46" height="46" viewBox="0 0 46 46" fill="none" stroke="#f1b27a" stroke-width="2"><rect x="8" y="3" width="14" height="6" rx="1"/><rect x="6" y="10" width="18" height="28" rx="3"/><circle cx="30" cy="30" r="11"/><path d="M22 38l16-16"/></svg>
      <h3>Tired of one-size-fits-all supplements?</h3>
      <p>At Verda, every formula is tailored to your unique mind-body type. No algorithms. No shortcuts. Just real doctors creating real tim-tested protocols-just for you. We don't do 'standard'. Verda formulas are hand-built by doctors to reflect your specific constitution, habits, and environment. You deserve precision-not guesswork</p>
    </article>

    <article class="abs pain" style="top:599px;height:202px">
      <svg width="46" height="46" viewBox="0 0 46 46" fill="none" stroke="#f1b27a" stroke-width="2"><path d="M6 3h26v38H6z"/><path d="M11 11h10M11 17h10M11 23h6"/><circle cx="33" cy="27" r="7"/><path d="M29 33v9l4-3 4 3v-9"/></svg>
      <h3>Being overcharged by unqualified self-professed experts?</h3>
      <p>The human psychology of valuing only that which we pay a lot for can be remedied with proven results. By setting an example-by making high-quality health care available to everyone. We hope that most will benefit.</p>
    </article>

    <a class="abs btn">BOOK NOW</a>
    <p class="abs center tested-note">Three minutes. No commitment. Much Clarity</p>
  </section>

  <section class="difference">
    <h2 class="abs diff-title">The Verda Difference</h2>
    <div class="abs diff-card" style="left:29px">
      <span class="diff-icon"><svg width="18" height="14" viewBox="0 0 18 14" fill="none" stroke="#555" stroke-width="1.3"><path d="M1 5l4-3 4 2 4-2 4 3-6 7z"/></svg></span>
      <div><h4>Precision You Can Trust</h4><p>Doctors cross-trained in time tested and modern science</p></div>
    </div>
    <div class="abs diff-card" style="left:283px">
      <span class="diff-icon"><svg width="18" height="14" viewBox="0 0 18 14" fill="none" stroke="#555" stroke-width="1.3"><path d="M1 8h4l4 3h6M5 8l3-5 4 3"/></svg></span>
      <div><h4>Care You Can Feel</h4><p>Plans crafted around your whole self &amp; life</p></div>
    </div>

    <div class="abs wheel">
      <svg class="abs" style="left:0;top:0" width="430" height="380" viewBox="0 0 430 380" fill="none">
        <path d="M130 20 A170 170 0 0 1 130 370" stroke="#dcdcdc" stroke-width="1.5"/>
        <path d="M120 64 A118 118 0 0 1 120 300" stroke="var(--peach-line)" stroke-width="9"/>
      </svg>
      <div class="abs wheel-core">
        1 Clinical Precision
        <b>What We Do</b>
        Doctors trained in classical herbal medicine and modern integrative science design every plan for you.
        <b>Why It Matters</b>
        Precise formulas reduce side effects, support lasting balance and help each client feel the difference.
      </div>
      <div class="abs wheel-item wheel-pill"><span class="wheel-icon"><i></i></span>1 Clinical Precision</div>
      <div class="abs wheel-item" style="left:243px;top:65px"><span class="wheel-icon"><i></i></span>2 High-Touch Personalization</div>
      <div class="abs wheel-item" style="left:276px;top:118px"><span class="wheel-icon"><i></i></span>3 No Harmful Cross-Reactions</div>
      <div class="abs wheel-item" style="left:282px;top:170px"><span class="wheel-icon"><i></i></span>4 Science-Guided Herbalism</div>
      <div class="abs wheel-item" style="left:274px;top:221px"><span class="wheel-icon"><i></i></span>5 Regulatory Integrity</div>
      <div class="abs wheel-item" style="left:243px;top:273px"><span class="wheel-icon"><i></i></span>6 Global Standard Sourcing</div>
      <div class="abs wheel-item" style="left:190px;top:321px"><span class="wheel-icon"><i></i></span>7 Evidence-Informed Guidance</div>
    </div>

    <div class="abs divider" style="top:605px"></div>

    <div class="abs step" style="top:636px">
      <div class="step-num">1</div>
      <svg width="30" height="84" viewBox="0 0 30 84" fill="none"><path d="M4 2 A40 40 0 0 1 4 82" stroke="var(--peach-line)" stroke-width="6"/></svg>
      <span class="step-dot"></span>
      <div class="step-text"><h4>Book</h4><p>Book now and fill out your secured details to be matched with a doctor specific to your needs</p></div>
    </div>
    <div class="abs step" style="top:742px">
      <div class="step-num">2</div>
      <svg width="30" height="84" viewBox="0 0 30 84" fill="none"><path d="M4 2 A40 40 0 0 1 4 82" stroke="var(--peach-line)" stroke-width="6"/></svg>
      <span class="step-dot"></span>
      <div class="step-text"><h4>Video Call</h4><p>Video Chat with your specialist</p></div>
    </div>
    <div class="abs step" style="top:848px">
      <div class="step-num">3</div>
      <svg width="30" height="84" viewBox="0 0 30 84" fill="none"><path d="M4 2 A40 40 0 0 1 4 82" stroke="var(--peach-line)" stroke-width="6"/></svg>
      <span class="step-dot"></span>
      <div class="step-text"><h4>Get Care + Unlimited Text</h4><p>Get customized diet, cleanse, lifestyle exercise, yoga &amp; meditation plans by your specialist + unlimited texting</p></div>
    </div>
    <div class="abs step" style="top:954px">
      <div class="step-num">4</div>
      <svg width="30" height="84" viewBox="0 0 30 84" fill="none"><path d="M4 2 A40 40 0 0 1 4 82" stroke="var(--peach-line)" stroke-width="6"/></svg>
      <span class="step-dot"></span>
      <div class="step-text"><h4>Monthly Video Follow UP</h4><p>Monthly Video call + essential care takes persistence</p></div>
    </div>

    <div class="abs divider" style="top:1073px"></div>
  </section>

  <section class="experts">
    <h2 class="abs center experts-title">Meet the Experts</h2>
    <p class="abs center experts-lead">Licensed, Global, Guided by science. Every Verda practitioner is trained in traditional medicine and modern clinical frameworks-bringing deep expertise to every personalized plan.</p>

    <div class="abs doc" style="left:31px;top:154px"><div class="doc-photo" role="img" aria-label="Portrait photo of the doctor"></div><h5>Dr. Clara Moss</h5><p>MBBS<br>BAMS<br>Oncology Director</p></div>
    <div class="abs doc" style="left:229px;top:154px"><div class="doc-photo" role="img" aria-label="Portrait photo of the doctor"></div><h5>Dr. Owen Hale</h5><p>MBBS<br>BAMS<br>Metabolic and<br>Musculoskeletal specialist</p></div>
    <div class="abs doc" style="left:31px;top:369px"><div class="doc-photo" role="img" aria-label="Portrait photo of the doctor"></div><h5>Dr. Lena Ford</h5><p>MBBS<br>BAMS<br>OBGYN and woman's health</p></div>
    <div class="abs doc" style="left:229px;top:369px"><div class="doc-photo" role="img" aria-label="Portrait photo of the doctor"></div><h5>Dr. Ivy Marsh</h5><p>MBBS<br>BAMS<br>Psychology specialist</p></div>

    <h2 class="abs center cert-title">Back by Expertise. Certified for Safety.<br>Trusted by Design</h2>
    <div class="abs cert" style="left:29px"><div class="cert-mark" style="border-radius:50%;background:#3a6fb0"></div>ISO 22000 &amp; EU Pharmacopoeia herbal standards</div>
    <div class="abs cert" style="left:159px"><div class="cert-mark" style="border-radius:50%;background:#1f3e8c"></div>GDPR-compliant data privacy</div>
    <div class="abs cert" style="left:295px"><div class="cert-mark" style="width:40px;height:44px;background:#1f3e8c"></div>Every supplement screened for drug interactions</div>

    <p class="abs bio-label">Bio markers and holistic integration</p>
    <div class="abs bio-photo" role="img" aria-label="Cupped hands holding glowing golden light"></div>
    <p class="abs bio-text">Bio markers are often not time tested nor really accurate when it comes to hormones because hormones fluctuate day to day if not hour to hour. We often don't catch imbalances or deficiencies until its far advanced and harder to treat. We employ lab bio markers along with time tested methods, often catching imbalance early on</p>
  </section>

  <footer class="footer" role="img" aria-label="Pink lotus flower among dark green leaves">
    <div class="abs glass quote-card">
      <p class="small">We're doctors, entrepreneurs and researchers with decades of experience. Verda is built for the soul of the modern man.</p>
      <p class="big">With loving support, we can blossom into our full potential.</p>
      <p class="sig">-Founder</p>
    </div>
    <div class="abs quote-badge"><svg width="30" height="26" viewBox="0 0 30 26" fill="var(--peach)"><path d="M2 2h11v11c0 6-4 10-9 11l-1-3c3-1 5-4 5-7H2zM17 2h11v11c0 6-4 10-9 11l-1-3c3-1 5-4 5-7h-6z"/></svg></div>
    <div class="abs glass tree-card">Ten trees planted per member per month = 120 trees per year per member. Our health depends on the health of Mother Nature - trees are proven to be the #1 way to purify and nourish the environment and help avert global warming.</div>
    <p class="abs center contact">Contact</p>
    <p class="abs center email">info@verda.net</p>
    <p class="abs center terms">Terms</p>
  </footer>

</main>
</body>
</html>
```